My project benefits Military, First Responders, Police, Fire, and Educators.

Contact Information for Business Card

2 Sided appointment card. Visual side will have my head shot with "Kestrel Works" in a bold graffic/text. I am picturing maybe the headshot applied to a filter that has a matrix effect where the picture is made up of data/numbers flowing vertically through the photo. I am of course open to other concepts as well. Side two will have contact info presented in an attractive visual complimenting the front.

```html
<!DOCTYPE html>
<html lang="en">
<head>
<meta charset="utf-8">
<title>Kestrel Works – Appointment Card</title>
<link rel="stylesheet" href="https://fonts.googleapis.com/css2?family=Source+Sans+3:ital,wght@0,400;0,600;1,400&display=swap">
<style>
  :root {
    --bg: #e9e8e5;
    --paper: #ffffff;
    --green: #17a673;
    --charcoal: #3a3b3d;
    --grey: #6a6a6a;
    --navy: #1f2a4a;
    --ink: #2b2b2b;
    --rule: #9fd9c2;
  }
  * { box-sizing: border-box; margin: 0; padding: 0; }
  html, body { width: 1200px; height: 900px; overflow: hidden; }
  body {
    background: var(--bg);
    font-family: "Source Sans 3", "Myriad Pro", sans-serif;
    color: var(--ink);
    position: relative;
  }
  .card {
    position: absolute;
    left: 260px;
    width: 680px;
    height: 388px;
    background: var(--paper);
    box-shadow: 0 6px 18px rgba(0,0,0,.18);
    overflow: hidden;
  }
  .card--appointment { top: 40px; }
  .card--contact { top: 472px; }

  /* Appointment side */
  .brand {
    position: absolute; top: 78px; left: 0; right: 0;
    text-align: center;
  }
  .brand__name {
    font-size: 44px; font-weight: 400; letter-spacing: 2px;
    color: var(--grey); text-transform: uppercase; line-height: 1;
  }
  .field {
    position: absolute; display: flex; align-items: flex-end;
    font-size: 18px; color: var(--ink); line-height: 1;
  }
  .field__line { flex: 1; border-bottom: 1.5px solid var(--rule); margin-left: 10px; }
  .field--name { top: 192px; left: 44px; width: 600px; }
  .field--date { top: 234px; left: 44px; width: 360px; }
  .field--time { top: 234px; left: 420px; width: 224px; }
  .field--date .field__line, .field--time .field__line { border-color: var(--green); }
  .notice {
    position: absolute; top: 286px; left: 44px; right: 30px;
    font-size: 20px; font-style: italic; color: var(--navy);
  }

  /* Contact side */
  .card__art { position: absolute; inset: 0; }
  .person { position: absolute; top: 24px; left: 84px; }
  .person__name { font-size: 25px; font-weight: 600; color: var(--green); line-height: 1.05; }
  .person__role { font-size: 18px; color: var(--ink); }
  .contacts {
    position: absolute; top: 212px; left: 40px; list-style: none;
    font-size: 18px; color: var(--ink);
  }
  .contacts li { display: flex; align-items: center; height: 26px; }
  .contacts svg { width: 14px; height: 14px; margin-right: 12px; fill: var(--green); }
  .headshot {
    position: absolute; left: 320px; top: 112px; width: 290px; height: 250px;
    background: linear-gradient(180deg, #d9b7a0 0%, #c79a7e 38%, #9aa4c4 55%, #1e2a44 78%, #18213a 100%);
    border-radius: 90px 90px 0 0;
  }
</style>
</head>
<body>

<section class="card card--appointment">
  <div class="brand">
    <div class="brand__name">Kestrel Works</div>
  </div>
  <div class="field field--name">Name :<span class="field__line"></span></div>
  <div class="field field--date">Date :<span class="field__line"></span></div>
  <div class="field field--time">Time:<span class="field__line"></span></div>
  <p class="notice">If unable to keep appointment, kindly give 24hrs notice.</p>
</section>

<section class="card card--contact">
  <div class="headshot" role="img" aria-label="Head and shoulders portrait of the managing director in a dark suit"></div>
  <svg class="card__art" width="680" height="388" viewBox="0 0 680 388" aria-hidden="true">
    <polygon points="0,22 40,22 20,48 0,48" fill="var(--charcoal)"/>
    <polygon points="42,22 76,22 60,62 16,62" fill="var(--green)"/>
    <polygon points="0,356 280,356 268,388 0,388" fill="var(--charcoal)"/>
    <polygon points="300,344 680,344 680,388 282,388" fill="var(--green)"/>
  </svg>
  <div class="person">
    <div class="person__name">Daniel Harlow</div>
    <div class="person__role">Managing Director</div>
  </div>
  <ul class="contacts">
    <li><svg viewBox="0 0 24 24"><path d="M6.6 10.8a15 15 0 0 0 6.6 6.6l2.2-2.2c.3-.3.7-.4 1-.2 1.1.4 2.3.6 3.6.6.6 0 1 .4 1 1V20c0 .6-.4 1-1 1A17 17 0 0 1 3 4c0-.6.4-1 1-1h3.5c.6 0 1 .4 1 1 0 1.3.2 2.5.6 3.6.1.3 0 .7-.2 1z"/></svg>044-987 654 321</li>
    <li><svg viewBox="0 0 24 24"><path d="M2 5h20v14H2z M2 5l10 8 10-8" /></svg>info@kestrelworks.com</li>
    <li><svg viewBox="0 0 24 24"><circle cx="12" cy="12" r="10"/></svg>www.kestrelworks.com</li>
  </ul>
</section>

</body>
</html>
```